Medical Company in need of a Modern Flyer design for new Wound Care clinic.

Tri-Fold modern flyer design for our Woundcare company. Logo and description of services can be found on our website; https://www.birchline-woundcare.com/

```html
<!DOCTYPE html>
<html lang="en">
<head>
<meta charset="utf-8">
<title>Birchline Wound Care – Tri-Fold Brochure</title>
<link href="https://fonts.googleapis.com/css2?family=Montserrat:wght@500;700;800&family=Raleway:wght@400;500&display=swap" rel="stylesheet">
<style>
  :root{
    --backdrop:#434343;
    --paper:#ffffff;
    --ink:#111111;
    --gold-dark:#b9852a;
    --gold-mid:#f3d27c;
    --gold-bright:#fdc73c;
    --gold-deep:#dc9b2c;
    --black:#000000;
  }
  html,body{margin:0;padding:0;width:873px;height:1200px;overflow:hidden;background:var(--backdrop);}
  .sheet{position:relative;width:960px;height:1320px;transform:scale(0.909375);transform-origin:0 0;font-family:'Raleway',sans-serif;color:var(--ink);}
  .panel{position:absolute;left:65px;width:830px;height:587px;background:var(--paper);overflow:hidden;}
  .panel--outside{top:49px;}
  .panel--inside{top:684px;}
  .panel__art{position:absolute;inset:0;width:830px;height:587px;display:block;}
  .heading{font-family:'Montserrat',sans-serif;font-weight:800;margin:0;position:absolute;line-height:1;}

  .brand{position:absolute;right:34px;top:106px;font-family:'Montserrat',sans-serif;font-weight:500;font-size:15px;letter-spacing:2.4px;color:var(--ink);}

  .contact{position:absolute;left:300px;width:230px;top:414px;text-align:center;}
  .contact .heading{position:static;font-size:21px;}
  .contact__icon{display:block;margin:18px auto 0;width:14px;height:14px;}
  .contact__phone{font-family:'Montserrat',sans-serif;font-weight:700;font-size:12.5px;margin-top:4px;}
  .contact__mail{margin-top:10px;}
  .contact__address{font-family:'Montserrat',sans-serif;font-weight:500;font-size:12.5px;line-height:16px;margin-top:4px;}

  .about .heading{left:16px;top:26px;font-size:24px;}
  .about__text{position:absolute;left:16px;top:69px;width:232px;font-size:11.3px;line-height:14.2px;margin:0;}

  .tagline{position:absolute;right:568px;top:290px;text-align:right;font-family:'Montserrat',sans-serif;font-weight:800;font-size:27.5px;line-height:30px;color:var(--paper);margin:0;}

  .services .heading{left:277px;width:276px;text-align:center;top:26px;font-size:24px;}
  .services__list{list-style:none;margin:0;padding:0;position:absolute;left:290px;top:70px;width:260px;}
  .services__item{position:relative;padding-left:32px;font-family:'Montserrat',sans-serif;font-weight:500;font-size:11.5px;line-height:14px;margin-bottom:14.5px;}
  .services__item::before,.services__item::after{content:"";position:absolute;background:var(--black);}
  .services__item::before{left:2px;top:5px;width:18px;height:5px;}
  .services__item::after{left:9px;top:-2px;width:5px;height:19px;}

  .therapy .heading{left:568px;top:284px;font-size:24px;line-height:29px;}
  .therapy__text{position:absolute;left:568px;top:361px;width:248px;font-size:11.3px;line-height:14.2px;margin:0;}
</style>
</head>
<body>
<div class="sheet">

  <section class="panel panel--outside">
    <svg class="panel__art" viewBox="0 0 830 587" aria-hidden="false">
      <defs>
        <linearGradient id="gold" x1="0" y1="0" x2="1" y2="1">
          <stop offset="0" stop-color="#b9852a"/>
          <stop offset="0.35" stop-color="#f3d27c"/>
          <stop offset="0.7" stop-color="#fdc73c"/>
          <stop offset="1" stop-color="#dc9b2c"/>
        </linearGradient>
        <linearGradient id="labTone" x1="0" y1="0" x2="1" y2="1">
          <stop offset="0" stop-color="#e4e6e7"/>
          <stop offset="0.5" stop-color="#b7c4c8"/>
          <stop offset="1" stop-color="#8fa9b0"/>
        </linearGradient>
        <linearGradient id="officeTone" x1="0" y1="0" x2="1" y2="1">
          <stop offset="0" stop-color="#e9edf1"/>
          <stop offset="0.5" stop-color="#9fb4c8"/>
          <stop offset="1" stop-color="#4f6f96"/>
        </linearGradient>
      </defs>
      <rect role="img" aria-label="Photo: clinician in protective gear touching floating medical icons" x="0" y="0" width="830" height="470" fill="url(#labTone)"/>
      <path fill="#ffffff" d="M330,0 H830 V160 C720,190 520,175 352,112 C470,95 520,50 330,0 Z"/>
      <rect role="img" aria-label="Photo: doctors and patient in a clinic office" x="553" y="168" width="277" height="300" fill="url(#officeTone)"/>
      <path fill="#ffffff" d="M0,452 C70,380 200,318 330,326 C430,333 500,378 555,400 L555,420 C490,392 420,350 330,344 C200,338 80,392 0,470 Z"/>
      <path fill="url(#gold)" d="M0,470 C80,392 200,338 330,344 C420,350 490,392 555,414 C660,440 760,420 830,350 V587 H0 Z"/>
      <path fill="#ffffff" d="M553,478 C650,492 760,470 830,398 V420 C760,492 650,520 553,503 Z"/>
    </svg>

    <div class="brand">BIRCHLINE WOUNDCARE</div>

    <div class="contact">
      <h2 class="heading">CONTACT US</h2>
      <svg class="contact__icon" viewBox="0 0 24 24" aria-hidden="true"><path fill="#111" d="M6.6 10.8a15.1 15.1 0 0 0 6.6 6.6l2.2-2.2a1 1 0 0 1 1-.25 11.4 11.4 0 0 0 3.6.57 1 1 0 0 1 1 1V20a1 1 0 0 1-1 1A17 17 0 0 1 3 4a1 1 0 0 1 1-1h3.5a1 1 0 0 1 1 1c0 1.25.2 2.45.57 3.57a1 1 0 0 1-.25 1z"/></svg>
      <div class="contact__phone">972-555-0147</div>
      <svg class="contact__icon contact__mail" viewBox="0 0 24 18" aria-hidden="true"><rect x="1" y="1" width="22" height="16" fill="#111"/><path d="M1 1 L12 10 L23 1" fill="none" stroke="#f6d27a" stroke-width="1.6"/></svg>
      <div class="contact__address">2180 Ridgeview Ln Ste 200<br>Dallas, TX 75230</div>
    </div>
  </section>

  <section class="panel panel--inside">
    <svg class="panel__art" viewBox="0 0 830 587">
      <defs>
        <linearGradient id="goldIn" x1="0" y1="0" x2="1" y2="1">
          <stop offset="0" stop-color="#b9852a"/>
          <stop offset="0.4" stop-color="#f3d27c"/>
          <stop offset="0.75" stop-color="#fdc73c"/>
          <stop offset="1" stop-color="#dc9b2c"/>
        </linearGradient>
        <linearGradient id="therapyTone" x1="0" y1="0" x2="1" y2="1">
          <stop offset="0" stop-color="#f1f1f0"/>
          <stop offset="0.6" stop-color="#d9c2b0"/>
          <stop offset="1" stop-color="#8fb7b4"/>
        </linearGradient>
        <linearGradient id="cuffTone" x1="0" y1="0" x2="1" y2="1">
          <stop offset="0" stop-color="#dfe2e5"/>
          <stop offset="0.6" stop-color="#f4efea"/>
          <stop offset="1" stop-color="#7fbfcb"/>
        </linearGradient>
        <linearGradient id="portraitTone" x1="0" y1="0" x2="1" y2="1">
          <stop offset="0" stop-color="#e8eef2"/>
          <stop offset="0.6" stop-color="#a7c1dc"/>
          <stop offset="1" stop-color="#6f97c6"/>
        </linearGradient>
      </defs>

      <rect role="img" aria-label="Photo: therapist supporting a patient's leg" x="0" y="300" width="277" height="287" fill="url(#therapyTone)"/>
      <path fill="#000000" d="M0,330 C25,272 110,241 200,241 C245,241 277,250 277,256 V420 C235,452 120,456 62,424 C30,405 8,372 0,345 Z"/>

      <rect role="img" aria-label="Photo: blood pressure cuff on a patient's arm" x="277" y="225" width="276" height="362" fill="url(#cuffTone)"/>
      <path fill="#ffffff" d="M277,236 C360,262 470,294 553,316 V336 C470,312 360,282 277,258 Z"/>
      <path fill="url(#goldIn)" d="M277,0 H553 V312 C470,290 360,260 277,236 Z"/>

      <rect role="img" aria-label="Photo: smiling surgeon in scrubs and cap" x="553" y="0" width="277" height="260" fill="url(#portraitTone)"/>
      <path fill="#ffffff" d="M553,246 C660,220 760,170 830,112 V587 H553 Z"/>

      <path fill="url(#goldIn)" d="M553,548 C660,540 770,520 830,470 V587 H553 Z"/>
      <path fill="#000000" d="M553,512 C630,532 740,538 830,478 V492 C740,560 630,562 553,540 Z"/>
    </svg>

    <div class="about">
      <h2 class="heading">ABOUT US</h2>
      <p class="about__text">At Birchline Wound Care, we specialize in managing outpatient wound care facilities throughout the Dallas/Fort Worth area. Partnering with hospitals and local rehabilitation units, we deliver the most advanced wound care treatments. Our commitment to quality care resonates through our collaboration with small practice family providers, ensuring personalized, effective treatment plans.</p>
    </div>

    <p class="tagline">YOUR<br>HEALTH IS<br>OUR PRIORITY</p>

    <div class="services">
      <h2 class="heading">OUR SERVICES</h2>
      <ul class="services__list">
        <li class="services__item">Hyperbaric Oxygen Therapy (HBO): A Cornerstone of Advanced Wound Care</li>
        <li class="services__item">Debridement</li>
        <li class="services__item">Advanced Wound Dressings</li>
        <li class="services__item">Bio-engineered Skin Substitutes</li>
        <li class="services__item">Compression Therapy and Edema Management</li>
      </ul>
    </div>

    <div class="therapy">
      <h2 class="heading">HYPERBARIC<br>OXYGEN THERAPY</h2>
      <p class="therapy__text">Hyperbaric Oxygen Therapy (HBO) is not just a treatment; it's a pivotal part of our comprehensive approach to wound healing at Birchline Wound Care. By delivering pure oxygen in a pressurized chamber, HBO therapy significantly increases the amount of oxygen in the blood, fostering an environment that accelerates the repair and regeneration of wounded tissues.</p>
    </div>
  </section>

</div>
</body>
</html>
```